Super elegant, crisp & clean Business card design required

We recently upgraded our branding - which is on our website - tavorelstudio.com

I would like a simple, yet elegant, clean business card design please.

The font of my logo is Cinzel - and because of the natural colour - it's best to have this on a black background.

I would like to have the back of the business card - with simply my logo.

PLEASE DO NOT SUBMIT A COMPLICATED / UNCLEAN DESIGN

Industry/Entity Type

Business

Contact Information for Business Card

Dalvik Ostrander Photography

Font styles to use
Other font styles liked:
• Cinzel

Requirements
Must have
• A backpage with nothing but my logo
• Simple design - stands out
Should not have
• Colour that dont align with my logo
• Over complicated '/ non symmetrical design

```html
<!DOCTYPE html>
<html lang="en">
<head>
<meta charset="utf-8">
<title>Dalvik Ostrander Photography — Business Card</title>
<link rel="stylesheet" href="https://fonts.googleapis.com/css2?family=Cinzel:wght@400;500&display=swap">
<style>
  :root {
    --backdrop: #33444c;
    --card: #07090a;
    --gold: #a8916b;
    --ink: #f4f2ee;
    --shadow: rgba(0, 0, 0, 0.45);
  }
  * { box-sizing: border-box; margin: 0; padding: 0; }
  html, body {
    width: 1200px;
    height: 900px;
    overflow: hidden;
    background: var(--backdrop);
  }
  .canvas {
    width: 1200px;
    height: 900px;
    display: flex;
    flex-direction: column;
    align-items: center;
    justify-content: center;
    gap: 36px;
    font-family: "Cinzel", serif;
  }
  .card {
    width: 700px;
    height: 400px;
    background: var(--card);
    box-shadow: 0 14px 30px var(--shadow);
    position: relative;
  }
  .card-front {
    display: flex;
    flex-direction: column;
    align-items: center;
    justify-content: center;
  }
  .mark-circle {
    width: 150px;
    height: 150px;
    border: 2px solid var(--gold);
    border-radius: 50%;
    margin-bottom: 34px;
  }
  .brand-name {
    color: var(--gold);
    font-size: 46px;
    font-weight: 400;
    letter-spacing: 1px;
    line-height: 1;
  }
  .brand-tagline {
    color: var(--gold);
    font-size: 20px;
    letter-spacing: 22px;
    margin-top: 6px;
    margin-right: -22px;
  }
  .card-back {
    padding: 68px 70px 0 78px;
    color: var(--ink);
  }
  .back-heading {
    font-size: 27px;
    font-weight: 400;
    text-align: center;
    letter-spacing: 0.5px;
    margin-bottom: 28px;
  }
  .contact-list { list-style: none; }
  .contact-item {
    display: flex;
    align-items: center;
    gap: 28px;
    height: 56px;
    font-size: 25px;
    letter-spacing: 0.5px;
  }
  .contact-item.phone { font-size: 34px; }
  .contact-icon {
    width: 44px;
    height: 38px;
    flex: none;
  }
</style>
</head>
<body>
<main class="canvas">
  <section class="card card-front" aria-label="Card front">
    <div class="mark-circle"></div>
    <h1 class="brand-name">Dalvik Ostrander</h1>
    <p class="brand-tagline">Photography</p>
  </section>

  <section class="card card-back" aria-label="Card back">
    <h2 class="back-heading">Dalvik Ostrander Photography</h2>
    <ul class="contact-list">
      <li class="contact-item web">
        <svg class="contact-icon" viewBox="0 0 44 38" aria-hidden="true">
          <g fill="none" stroke="var(--gold)" stroke-width="2.6">
            <circle cx="20" cy="19" r="15"/>
            <ellipse cx="20" cy="19" rx="6.5" ry="15"/>
            <line x1="5" y1="19" x2="35" y2="19"/>
            <line x1="8" y1="11" x2="32" y2="11"/>
            <line x1="8" y1="27" x2="32" y2="27"/>
          </g>
        </svg>
        <span>tavorelstudio.com</span>
      </li>
      <li class="contact-item email">
        <svg class="contact-icon" viewBox="0 0 44 38" aria-hidden="true">
          <g fill="none" stroke="var(--gold)" stroke-width="2.6" stroke-linejoin="round">
            <rect x="3" y="7" width="38" height="25"/>
            <polyline points="3,7 22,22 41,7"/>
            <line x1="3" y1="32" x2="17" y2="18"/>
            <line x1="41" y1="32" x2="27" y2="18"/>
          </g>
        </svg>
        <span>do.photography@tavorelmail.com</span>
      </li>
      <li class="contact-item phone">
        <svg class="contact-icon" viewBox="0 0 44 38" aria-hidden="true">
          <path fill="var(--gold)" d="M9 4 L15 3 L18 12 L14 15 C16 21 20 25 26 27 L29 23 L38 26 L37 32 C35 35 30 36 25 34 C15 30 8 22 6 13 C5 9 6 6 9 4 Z"/>
        </svg>
        <span>07700 900318</span>
      </li>
      <li class="contact-item social">
        <svg class="contact-icon" viewBox="0 0 44 38" aria-hidden="true">
          <rect x="3" y="0" width="38" height="38" fill="var(--gold)"/>
        </svg>
        <span>tavorelstudio</span>
      </li>
    </ul>
  </section>
</main>
</body>
</html>
```